Bramblewick Co Leaflet. A5 2-sided Flyer for a UK Lawn Treatment Company

I need an A5 two-side leaflet / flyer designed for my Lawn Treatment company. The leaflet will be for door-drops so quick impact needed. Full colour, both sides. I provide lawn treatments to customers in the Exeter area of Devon. I would like to design to be clear, fresh and reflect the joy a good lawn and garden can bring.

Target Market(s)

Home Owners. 30-80 Years. Familys

Font styles to use
Sans Serif

Colors
9bcb3c
f78f20
ec1f27
33a6d7

Requirements
Must have
• Good front page picture
• Logo
• Contact details on front.
• Call to Action
• More details in Text file included in design.
Nice to have
• Clipart of a family / lady enjoying a lawn.

```html
<!DOCTYPE html>
<html lang="en">
<head>
<meta charset="utf-8">
<title>Bramblewick Co Leaflet</title>
<link href="https://fonts.googleapis.com/css2?family=Lato:wght@400;700&family=Lora:wght@400;700&display=swap" rel="stylesheet">
<style>
  :root {
    --bg: #e4e4e4;
    --green-dark: #0e4a12;
    --green: #2f7a33;
    --green-mid: #3d8a3c;
    --gold: #f0ac0c;
    --navy: #0e2f6b;
    --ink: #1d1d1d;
    --paper: #f4f4f4;
    --white: #ffffff;
  }
  * { box-sizing: border-box; margin: 0; padding: 0; }
  html, body { width: 1200px; height: 1200px; overflow: hidden; }
  body { background: var(--bg); font-family: 'Lato', sans-serif; position: relative; }

  .page { position: absolute; top: 277px; width: 493px; height: 690px; overflow: hidden; box-shadow: 0 6px 16px rgba(0,0,0,.25); }
  .page--front { left: 75px; }
  .page--back { left: 633px; background: var(--paper); }

  /* front */
  .front-photo { position: absolute; inset: 0; background: linear-gradient(180deg, #cfd9c4 0%, #5f9848 14%, #3f7d2e 40%, #4f8a32 58%, #2a5a1f 72%, #1c3e18 100%); }
  .brand-name { position: absolute; top: 240px; left: 0; width: 100%; text-align: center; color: var(--white); font: 700 36px 'Lato', sans-serif; letter-spacing: 1px; }
  .front-headline { position: absolute; top: 394px; left: 0; width: 100%; text-align: center; font-family: 'Lora', serif; font-weight: 700; }
  .front-headline .kicker { display: block; color: var(--gold); font-size: 24px; text-transform: uppercase; }
  .front-headline .main { display: block; color: var(--white); font-size: 26px; margin-top: 2px; }
  .front-points { position: absolute; top: 466px; left: 0; width: 100%; text-align: center; color: var(--white); font-size: 13px; line-height: 16.5px; }
  .wave { position: absolute; inset: 0; width: 100%; height: 100%; }
  .front-contact { position: absolute; top: 630px; left: 0; width: 100%; text-align: center; color: var(--white); font-family: 'Lora', serif; font-size: 13.5px; line-height: 19px; }

  /* back */
  .back-column { position: absolute; left: 0; top: 0; width: 230px; height: 690px; background: linear-gradient(180deg, var(--green) 0%, var(--green-mid) 50%, var(--green) 100%); padding: 22px 18px 0 20px; color: var(--white); }
  .section-title { font-family: 'Lora', serif; font-weight: 700; color: var(--gold); font-size: 12px; line-height: 15px; text-transform: uppercase; margin-bottom: 9px; }
  .section-text { font-size: 8.2px; line-height: 11px; text-align: justify; margin-bottom: 30px; }
  .section-text.tight { margin-bottom: 16px; }
  .treatments { display: flex; gap: 14px; font-size: 8.2px; line-height: 12.4px; }
  .treatments ul { list-style: none; }
  .treatments li { position: relative; padding-left: 11px; }
  .treatments li::before { content: ""; position: absolute; left: 0; top: 4.5px; width: 3.5px; height: 3.5px; border-radius: 50%; background: var(--gold); }
  .treatments ul:last-child { width: 92px; }
  .closing-line { margin-top: 40px; text-align: center; font-family: 'Lora', serif; font-weight: 700; color: var(--gold); font-size: 12px; line-height: 15px; }

  .testimonials { position: absolute; left: 246px; top: 30px; width: 224px; color: var(--ink); font-size: 8px; line-height: 11px; }
  .testimonial { text-align: justify; margin-bottom: 22px; }
  .testimonial cite { font-style: normal; font-weight: 700; color: var(--navy); font-size: 10px; margin-left: 6px; }
  .call-block { position: absolute; left: 230px; top: 464px; width: 263px; text-align: center; font-family: 'Lora', serif; font-weight: 700; line-height: 29px; }
  .call-block .call, .call-block .phone { color: var(--green); font-size: 25px; }
  .call-block .today { color: var(--ink); font-size: 24px; }
  .website { position: absolute; top: 646px; left: 230px; width: 263px; text-align: center; color: var(--white); font-family: 'Lora', serif; font-weight: 700; font-size: 13px; letter-spacing: 2.4px; }
</style>
</head>
<body>

<section class="page page--front">
  <div class="front-photo" role="img" aria-label="Photograph of a landscaped garden with a striped lawn, gravel path and lush trees"></div>
  <div class="brand-name">Bramblewick Co</div>
  <h1 class="front-headline">
    <span class="kicker">Treatments and advice to</span>
    <span class="main">keep your lawn looking nice</span>
  </h1>
  <p class="front-points">Brand new to the area!<br>8 Years experience maintaining the finest lawns of Cheshire<br>Complete Satisfaction Guarantee</p>
  <svg class="wave" viewBox="0 0 493 690" preserveAspectRatio="none" aria-hidden="true">
    <path d="M0 568 C80 545 170 528 250 540 C330 552 420 585 493 598 L493 690 L0 690Z" fill="var(--white)"/>
    <path d="M0 562 C90 530 180 520 260 535 C340 550 420 580 493 592 L493 598 C420 592 330 566 250 556 C170 546 80 555 0 566Z" fill="var(--gold)"/>
    <path d="M0 578 C90 552 190 555 280 580 C360 602 430 610 493 604 L493 690 L0 690Z" fill="var(--green-dark)"/>
  </svg>
  <p class="front-contact">Call today on 01632 960418 or text 07700 900312<br>To book your lawn survey bramblewickco.co.uk</p>
</section>

<section class="page page--back">
  <div class="back-column">
    <h2 class="section-title">For a beautiful<br>weed-free lawn</h2>
    <p class="section-text">Call Bramblewick Co today and start your journey to a wonderful, lush, green lawn you and your family can enjoy. Arrange a no-obligation lawn survey and quotation at a time to suit you. Call 01632 960418 now.</p>
    <h2 class="section-title">I will understand<br>your lawn</h2>
    <p class="section-text tight">Every lawn is unique. I take time to gain a comprehensive understanding of your lawn and its situation. I will also listen to you and understand your problems and your aspirations for your grass.</p>
    <h2 class="section-title">Your lawn treatments</h2>
    <p class="section-text tight">I will creat a custom treatment programme tailored to your lawn. I may also recommend some remedial treatments to correct any existing problems. There is no contract to sign. I guarantee all treatments.</p>
    <h2 class="section-title">Industry-leading<br>lawn care</h2>
    <p class="section-text tight">I have 8 years of experience in the leading edge of domestic lawn care. I have a comprehensive range of treatments including</p>
    <div class="treatments">
      <ul>
        <li>Scarification</li><li>Aeration</li><li>Moss Control</li><li>Overseeding</li><li>Top Dressing</li><li>Lawn Repairs</li>
      </ul>
      <ul>
        <li>Fertilisation &amp; Weed Control</li><li>Pest and Disease Management</li><li>Special Event Preparation</li>
      </ul>
    </div>
    <p class="closing-line">SAVE TIME AND MONEY<br>AND LEAVE YOUR LAWN<br>TO AN EXPERT</p>
  </div>

  <div class="testimonials">
    <p class="testimonial">Thank you for keeping our lawn in great shape for so long, I've been really pleased with how it has looked since you took care of it. <cite>- Owen</cite></p>
    <p class="testimonial">My lawn has never looked better since the day that you started to look after it for me. <cite>- Mr. Pryce</cite></p>
    <p class="testimonial">We are so grateful for your skill over the years. We've seen our lawn thrive and you changed a neglected difficult garden to one that everyone comments on. <cite>- Morwenna</cite></p>
    <p class="testimonial">Thank you for the lawn service you have provided over the years. It is reassuring to have you come round as I know you carried out the service as promised unlike other lawn service companies I have dealt with. <cite>- Gareth</cite></p>
    <p class="testimonial">We have very much appreciated your service over the last four years, and especially value your reliability and perennial cheerfulness! <cite>- Clifford</cite></p>
    <p class="testimonial">It has been a pleasure to do business with you over the last few years and the lawn you leave us with is infinitely healthier and more attractive than the lawn you inherited! <cite>- Rosalind</cite></p>
    <p class="testimonial">Your company have been fantastic. Reliable, good advice, effective treatments and you are very knowledgeable about lawns. You really do know what you are talking about! Cannot recommend you highly enough. <cite>- Gareth</cite></p>
  </div>

  <div class="call-block">
    <div class="call">CALL</div>
    <div class="phone">01632 960418</div>
    <div class="today">TODAY</div>
  </div>

  <svg class="wave" viewBox="0 0 493 690" preserveAspectRatio="none" aria-hidden="true">
    <path d="M0 610 C90 622 200 612 290 592 C360 578 420 585 493 615 L493 690 L0 690Z" fill="var(--white)"/>
    <path d="M0 604 C90 616 200 604 290 585 C360 572 420 580 493 612 L493 618 C420 592 360 590 290 600 C200 614 90 628 0 618Z" fill="var(--gold)"/>
    <path d="M0 635 C100 640 200 628 290 612 C370 598 430 600 493 620 L493 690 L0 690Z" fill="var(--green)"/>
  </svg>
  <div class="website">www.bramblewickco.co.uk</div>
</section>

</body>
</html>
```